ZEPRILO.COM is a premium domain sales company. Our competitors are companies like vastplots.example, getparcels.example, peerwords.example. Our current site is at www.zeprilos.example.

We want to have the ability to search for domains, to highlight special offers and have some testimonials on the index page.

The logo for the site is attached.

Please be sure that the order form fits on the screen without scrolling the page. I want the entire form, including the submit button to fit without any page scrolling.

Delivered product - INDEX PAGE, ORDER FORM AND CONTENT PAGE PSDs.

Target Market(s)

Small to Medium business professionals

Industry/Entity Type

It Company

Requirements
Must have
• 1. List of domains for sale
2. Simple search box with button to run the search
3. link for advanced search
4. testimonial area. Note - this can be a small box where a different testimonial is displayed on each page load.
Nice to have
• Would like the site to have some white space. Don't want a heavily packed website. Give it an "airy" feel.

```html
<!DOCTYPE html>
<html lang="en">
<head>
<meta charset="utf-8">
<title>ZEPRILO.COM — Premium Domains</title>
<link rel="stylesheet" href="https://fonts.googleapis.com/css2?family=Roboto:ital,wght@0,400;0,500;0,700;1,400&display=swap">
<style>
:root{
  --grass-dark:#1f4a12;
  --grass-mid:#3f8a22;
  --grass-light:#5aa532;
  --footer-bg:#1e1e1e;
  --footer-box:#191919;
  --blue-top:#3a8de0;
  --blue-bottom:#0d4c9c;
  --blue-deep:#0a3270;
  --navy-text:#0b2c5c;
  --green-top:#25b25a;
  --green-bottom:#077a35;
  --paper:#efede8;
  --row-grey:#d4d2ce;
  --pill-grey:#c3c1bd;
  --frame-dark:#3a3a3a;
  --field-grey:#bcbab6;
  --text-dark:#333;
  --text-muted:#8a8a8a;
  --white:#fff;
}
*{box-sizing:border-box;margin:0;padding:0}
html,body{width:1200px;height:625px;overflow:hidden}
body{position:relative;font-family:'Roboto',Arial,sans-serif;background:var(--footer-bg);color:var(--text-dark)}
.abs{position:absolute}
.hero-backdrop{left:0;top:0;width:1200px;height:453px;
  background:radial-gradient(ellipse at 50% 55%,var(--grass-light) 0%,var(--grass-mid) 45%,var(--grass-dark) 100%);}
.hero-backdrop::after{content:"";position:absolute;left:0;right:0;bottom:0;height:4px;background:#0f2608}
.green-btn{background:linear-gradient(var(--green-top),var(--green-bottom));color:var(--white);border-radius:12px;display:flex;align-items:center;justify-content:center;box-shadow:0 1px 2px rgba(0,0,0,.4)}
.blue-grad{background:linear-gradient(var(--blue-top),var(--blue-bottom))}

/* header */
.advanced-search{left:802px;top:11px;width:85px;height:16px;font-size:8px;gap:4px}
.search-bar{left:395px;top:32px;width:511px;height:40px;border-radius:0 14px 14px 0;box-shadow:0 2px 4px rgba(0,0,0,.4)}
.brand{left:294px;top:31px;width:118px;height:44px;background:var(--white);border-radius:22px;display:flex;align-items:center;justify-content:center;gap:5px;box-shadow:0 2px 4px rgba(0,0,0,.35)}
.brand-mark{width:10px;height:10px;border-radius:50%;background:var(--green-bottom)}
.brand-name{font-size:15px;font-weight:700;color:var(--navy-text)}
.search-label{left:443px;top:46px;font-size:12px;font-weight:700;color:var(--navy-text);letter-spacing:.2px}
.search-field{left:600px;top:41px;width:293px;height:25px;background:var(--blue-deep);border-radius:12px;box-shadow:inset 0 1px 3px rgba(0,0,0,.6)}
.search-text{left:617px;top:47px;font-size:10px;color:#dfe8f5}
.tld-select{left:831px;top:43px;width:56px;height:20px;font-size:10px;gap:10px;border-radius:10px}
.register-box{left:913px;top:37px;width:135px;height:33px;border-radius:16px;box-shadow:0 2px 4px rgba(0,0,0,.4)}
.register-tick{left:928px;top:47px}
.register-label{left:950px;top:42px;font-size:8px;color:#d5e4f7}
.register-price{left:950px;top:51px;font-size:12px;font-weight:700;color:var(--white)}
.register-price sup{font-size:7px}
.register-price small{font-size:8px;font-weight:400}
.register-go{left:1007px;top:41px;width:34px;height:24px}

/* panels */
.tab{height:36px;border-radius:16px 16px 4px 4px;color:var(--white);font-size:13px;font-weight:500;display:flex;align-items:center;justify-content:center;box-shadow:0 2px 3px rgba(0,0,0,.4);z-index:2}
.tab-green{background:linear-gradient(var(--green-top),var(--green-bottom))}
.listing-card{left:294px;top:146px;width:212px;height:226px;background:var(--paper)}
.panel-foot{background:var(--frame-dark);box-shadow:0 3px 6px rgba(0,0,0,.4)}
.listing-foot{left:294px;top:372px;width:212px;height:29px}
.listing-row{left:306px;width:187px;height:22px;display:flex;align-items:center;padding-left:13px;font-size:9.5px}
.listing-row.striped{background:var(--row-grey)}
.listing-row.featured .domain{color:#1f5fae}
.price-pill{position:absolute;right:6px;width:45px;height:16px;border-radius:8px;background:var(--pill-grey);font-size:9px;display:flex;align-items:center;justify-content:center;box-shadow:inset 0 1px 2px rgba(0,0,0,.25)}
.price-pill sup{font-size:6px}
.price-pill small{font-size:5.5px;margin-left:2px}
.featured .price-pill{background:var(--blue-bottom);color:var(--white)}
.offer-flag{left:492px;top:222px;width:46px;height:21px;background:var(--green-bottom);clip-path:polygon(12% 0,100% 0,100% 100%,12% 100%,0 50%);color:var(--white);font-size:6.5px;font-weight:700;line-height:7px;text-align:center;padding:3px 0 0 6px}
.more-link{left:356px;top:381px;font-size:9px;color:#ccc}
.more-go{left:460px;top:377px;width:28px;height:19px}

.order-frame{left:543px;top:146px;width:363px;height:255px}
.order-card{left:556px;top:151px;width:337px;height:221px;background:var(--paper)}
.field-label{left:575px;font-size:9.5px}
.field{left:694px;width:175px;height:28px;background:var(--field-grey);box-shadow:inset 0 1px 3px rgba(0,0,0,.35);font-size:9.5px;padding:9px 13px}
.month,.day{top:336px;width:45px;height:18px;font-size:9px;gap:6px;border-radius:9px}
.cvv{left:812px;top:330px;width:57px;height:28px;font-size:9.5px;padding:9px 0 0 19px;background:var(--field-grey);box-shadow:inset 0 1px 3px rgba(0,0,0,.35)}
.terms-note{left:602px;top:381px;font-size:9px;color:#ccc}
.terms-note u{color:#eee}
.order-btn{left:803px;top:376px;width:66px;height:20px;font-size:9px;gap:8px}

/* footer */
.testimonial{left:300px;top:474px;width:600px;text-align:center;font-size:10.5px;font-style:italic;line-height:16px;color:#8d8d8d}
.testimonial-author{left:300px;top:521px;width:600px;text-align:center;font-size:8.5px;color:#6f6f6f}
.copyright-bar{left:294px;top:578px;width:612px;height:47px;background:var(--footer-box);border-radius:3px 3px 0 0;font-size:8px;color:#777;text-align:center;padding-top:20px}
.copyright-bar span{color:var(--green-top)}
</style>
</head>
<body>
<div class="abs hero-backdrop" role="img" aria-label="Soft-focus background photo of green grass"></div>

<header>
  <a class="abs green-btn advanced-search">advanced search
    <svg width="9" height="8" viewBox="0 0 9 8"><circle cx="3" cy="4" r="2.5" fill="none" stroke="#fff" stroke-width="1.5"/><circle cx="7.5" cy="2" r="1.2" fill="#fff"/></svg></a>
  <div class="abs search-bar blue-grad"></div>
  <div class="abs brand"><span class="brand-mark"></span><span class="brand-name">ZEPRILO.COM</span></div>
  <div class="abs search-label">SEARCH FOR YOUR DOMAIN:</div>
  <div class="abs search-field"></div>
  <div class="abs search-text">www.yourdomainname</div>
  <div class="abs green-btn tld-select">.com
    <svg width="8" height="5" viewBox="0 0 8 5"><path d="M1 1l3 3 3-3" fill="none" stroke="#fff" stroke-width="1.3"/></svg></div>
  <div class="abs register-box blue-grad"></div>
  <svg class="abs register-tick" width="12" height="10" viewBox="0 0 12 10"><path d="M1 5l3.5 3.5L11 1" fill="none" stroke="#0a3270" stroke-width="1.6"/></svg>
  <div class="abs register-label">Register for:</div>
  <div class="abs register-price">$ 29<sup>.99</sup> <small>/yr.</small></div>
  <a class="abs green-btn register-go"><svg width="10" height="9" viewBox="0 0 10 9"><path d="M1 1l3.5 3.5L1 8M5 1l3.5 3.5L5 8" fill="none" stroke="#fff" stroke-width="1.6"/></svg></a>
</header>

<main>
  <section>
    <h2 class="abs tab tab-green" style="left:313px;top:128px;width:174px">Latest Domains for Sale</h2>
    <div class="abs listing-card"></div>
    <div class="abs listing-row" style="top:176px"><span class="domain">plotname.example</span><span class="price-pill">12<sup>99</sup><small>/yr.</small></span></div>
    <div class="abs listing-row striped" style="top:199px"><span class="domain">lumenfind.example</span><span class="price-pill">29<sup>50</sup><small>/yr.</small></span></div>
    <div class="abs listing-row featured" style="top:221px"><span class="domain">orchardly.example</span><span class="price-pill">8<sup>99</sup><small>/yr.</small></span></div>
    <div class="abs offer-flag">HALF<br>PRICE!</div>
    <div class="abs listing-row striped" style="top:244px"><span class="domain">zeprilo.com</span><span class="price-pill">239<sup>90</sup><small>/yr.</small></span></div>
    <div class="abs listing-row" style="top:266px"><span class="domain">sitecraft.example</span><span class="price-pill">12<sup>99</sup><small>/yr.</small></span></div>
    <div class="abs listing-row striped" style="top:289px"><span class="domain">howtomake.example</span><span class="price-pill">29<sup>50</sup><small>/yr.</small></span></div>
    <div class="abs listing-row" style="top:311px"><span class="domain">steelhero.example</span><span class="price-pill">8<sup>99</sup><small>/yr.</small></span></div>
    <div class="abs listing-row striped" style="top:334px"><span class="domain">namequest.example</span><span class="price-pill">239<sup>90</sup><small>/yr.</small></span></div>
    <div class="abs panel-foot listing-foot"></div>
    <div class="abs more-link">show me more domains</div>
    <a class="abs green-btn more-go"><svg width="10" height="9" viewBox="0 0 10 9"><path d="M1 1l3.5 3.5L1 8M5 1l3.5 3.5L5 8" fill="none" stroke="#fff" stroke-width="1.6"/></svg></a>
  </section>

  <section>
    <div class="abs panel-foot order-frame"></div>
    <div class="abs order-card"></div>
    <h2 class="abs tab blue-grad" style="left:656px;top:128px;width:137px">Buy Your Domain</h2>
    <div class="abs field-label" style="top:189px">Your name and surname:</div>
    <div class="abs field" style="top:180px">Your name and surname:</div>
    <div class="abs field-label" style="top:227px">Domain name:</div>
    <div class="abs field" style="top:218px">www.orchardly.example</div>
    <div class="abs field-label" style="top:264px">Full address:</div>
    <div class="abs field" style="top:255px">27 Fern Row, Maple Falls</div>
    <div class="abs field-label" style="top:302px">Card Number:</div>
    <div class="abs field" style="top:293px">23823 12934 123402 314912</div>
    <div class="abs field-label" style="top:339px">Expiration date &amp; CVV:</div>
    <div class="abs field" style="top:330px;width:118px"></div>
    <div class="abs green-btn month" style="left:706px">01 <svg width="8" height="5" viewBox="0 0 8 5"><path d="M1 1l3 3 3-3" fill="none" stroke="#fff" stroke-width="1.3"/></svg></div>
    <div class="abs green-btn day" style="left:756px">16 <svg width="8" height="5" viewBox="0 0 8 5"><path d="M1 1l3 3 3-3" fill="none" stroke="#fff" stroke-width="1.3"/></svg></div>
    <div class="abs cvv">368</div>
    <div class="abs terms-note">I agree with all the <u>terms</u> by pressing order button</div>
    <a class="abs green-btn order-btn">ORDER <svg width="10" height="9" viewBox="0 0 10 9"><path d="M1 1l3.5 3.5L1 8M5 1l3.5 3.5L5 8" fill="none" stroke="#fff" stroke-width="1.6"/></svg></a>
  </section>
</main>

<footer>
  <blockquote class="abs testimonial">"Phasellus sollicitudin risus vitae massa rhoncus tincidunt sed et odio. Donec eget lacus ut risus feugiat iaculis. Donec eu mauris augue. Integer pulvinar, turpis ut sagittis bibendum, ligula est consequat est, at pharetra ipsum nibh facilisis nulla."</blockquote>
  <div class="abs testimonial-author">Name, Surname: CEO Orchardly</div>
  <div class="abs copyright-bar">Copyright 2013 © <span>Zeprilo.com</span></div>
</footer>
</body>
</html>
```